KESTREL BOILWORKS business card

We need a new business card for our company "Kestrel Boilworks". The company is very simple, we supply bulk heated water to the oilfield and industry. I have included a few images of cards that I like so that you have an idea of the direction I want to go. I will leave fonts up to the designer. I have also included our logo.
Updates

Hello Designers,  if there are any more submissions coming in you might consider using other background colors than black.  I am looking for a little bit of variety before making the decision.

Thanks,

Dean

Sorry, I meant to say background colors other than just black and white.

Thanks,

Dean

Target Market(s)

Ages 20 to 60. Oilfield consultants and Oil and Gas Companies

Industry/Entity Type

Business

Font styles to use
Sans Serif

Requirements
Must have
• Dean Varga

email info@kestrelboilworks-mail.com

Phone # 780-555-3817
Fax 780-555-2964

Site 317, Box 4, Comp 2, RR5
Corvin Falls, AB, T9K 4P3

11-07-52-3 W4M
Hwy 734 Between RR57 & RR58

**Must have our logo

Nice to have
• Would be nice to have " Bulk Heated Water" somewhere on the card

The logo with the flame large across the background might look ok? The name of the company is KESTREL BOILWORKS, but it probably isn't necessary to have the hot water under the logo all the time if you decide it looks better. As long as it is included somewhere on the card. The style of the Kestrel can change slightly (ie:; can be slanted).

The colors of the logo can change, but it might be nice to have the original color and logo somewhere small (corner?)

```html
<!DOCTYPE html>
<html lang="en">
<head>
<meta charset="utf-8">
<title>Kestrel Boilworks – Business Card</title>
<link rel="stylesheet" href="https://fonts.googleapis.com/css2?family=Open+Sans:wght@400;700&display=swap">
<style>
  :root {
    --page: #ffffff;
    --card-grey: #cccdce;
    --card-black: #020205;
    --swoosh-blue: #0f87bd;
    --brand-orange: #ee4323;
    --text-grey: #9a9b9e;
    --rule-grey: #8e8f92;
  }
  html, body {
    margin: 0;
    padding: 0;
    width: 1000px;
    height: 1200px;
    overflow: hidden;
    background: var(--page);
    font-family: "Open Sans", sans-serif;
  }
  .canvas {
    position: relative;
    width: 1000px;
    height: 1200px;
  }
  .card {
    position: absolute;
    left: 65px;
    width: 870px;
    height: 503px;
    overflow: hidden;
  }
  .card svg.card-bg {
    position: absolute;
    inset: 0;
    width: 100%;
    height: 100%;
  }
  .card--front { top: 99px; background: var(--card-grey); }
  .card--back  { top: 621px; background: var(--card-black); }

  .brand {
    position: absolute;
    left: 0;
    right: 0;
    top: 310px;
    display: flex;
    align-items: center;
    justify-content: center;
    gap: 18px;
  }
  .brand-dot {
    width: 44px;
    height: 44px;
    border-radius: 50%;
    background: var(--swoosh-blue);
  }
  .brand-name {
    margin: 0;
    font-size: 54px;
    font-weight: 700;
    color: var(--brand-orange);
    letter-spacing: 0.5px;
    line-height: 1;
  }

  .contact {
    position: absolute;
    inset: 0;
    color: var(--text-grey);
    text-align: center;
  }
  .contact-name {
    position: absolute;
    left: 207px;
    width: 461px;
    top: 52px;
    margin: 0;
    font-size: 70px;
    font-weight: 400;
    line-height: 1;
    padding-bottom: 22px;
    border-bottom: 2px solid var(--rule-grey);
  }
  .contact-block {
    position: absolute;
    left: 0;
    right: 0;
    margin: 0;
    font-size: 31px;
    line-height: 44px;
  }
  .contact-block--mail { top: 156px; }
  .contact-block--site { top: 288px; }
  .contact-email {
    position: absolute;
    left: 0;
    right: 0;
    top: 397px;
    margin: 0;
    font-size: 28px;
  }
  .contact-phone, .contact-fax {
    position: absolute;
    top: 445px;
    margin: 0;
    font-size: 29px;
    white-space: nowrap;
  }
  .contact-phone { left: 77px; }
  .contact-fax   { left: 525px; }
</style>
</head>
<body>
<main class="canvas">

  <section class="card card--front" aria-label="Card front">
    <svg class="card-bg" viewBox="0 0 870 503" preserveAspectRatio="none" aria-hidden="true">
      <path d="M0 0 H835 C380 10 20 110 0 500 Z" fill="var(--swoosh-blue)"/>
    </svg>
    <div class="brand">
      <span class="brand-dot" aria-hidden="true"></span>
      <h1 class="brand-name">KESTREL BOILWORKS</h1>
    </div>
  </section>

  <section class="card card--back" aria-label="Card back">
    <svg class="card-bg" viewBox="0 0 870 503" preserveAspectRatio="none" aria-hidden="true">
      <path d="M0 0 H870 V3 C150 0 0 20 0 500 Z" fill="var(--swoosh-blue)"/>
    </svg>
    <div class="contact">
      <h2 class="contact-name">Dean Varga</h2>
      <p class="contact-block contact-block--mail">Site 317, Box 4, Comp 2, RR5<br>Corvin Falls, AB, T9K 4P3</p>
      <p class="contact-block contact-block--site">11-07-52-3 W4M<br>Hwy 734 Between RR57 &amp; RR58</p>
      <p class="contact-email">email: info@kestrelboilworks-mail.com</p>
      <p class="contact-phone">Phone : # 780-555-3817</p>
      <p class="contact-fax">Fax : 780-555-2964</p>
    </div>
  </section>

</main>
</body>
</html>
```